Poster / Flyer / Advertisement for Frosk Brew Chill (Unique Product!)

We’re selling alcoholic (7.5%) flavored ice for beer…for example, you might try our Lime flavor in a Valdor. We need a great ad/poster…please follow these guidelines:
USE THE PRODUCT PHOTO & KEEP IT SIMPLE!
Use the attached “action shot” of our product prominently. I prefer just the glass of beer, so turn off the layer with the beer bottle. Photoshop in a great background and KEEP IT SIMPLE - the product shot pretty much says it all. Find a great background, add the words “Your beer is getting warm”, and layer in some of our branding (see below). That’s it! Don’t make the poster too busy!
USE OUR CURRENT BRANDING
I’ve attached AI files with all of our branding. Layer in the pattern used on the packaging, our logo, and probably the “Frosk Chill” banner. Also, given that our most popular flavor is Lime in a Valdor, I would look for a background that helps express that (just a thought, it’s up to you to make it look good!).
MAKE IT VERSATILE
We need this to be versatile and easily scale up or down in size for various applications such as:
1) Large format poster for the front window of a convenience store
2) Smaller format for poster ads in bars/restaurants
3) Even smaller format for window clings that go on the glass doors of beer coolers
I also want the words for the poster to be easily changeable for the different applications:
1) Bar – I would use the tagline “Your beer is getting warm”
2) Convenience Store – I would use the line “Don’t drink warm beer…check the freezer!” or something similar. Just need it easy to change
Updates
Project Deadline Extended
Reason: Still deciding on designs. Need time to review with business partners. Thanks all!
Target Market(s)
Beer drinkers - especially those that like fruity beers like summer shandy
Industry/Entity Type
Brewery
Font styles to use
Other font styles liked:
- Use attached fonts!
Colors
Designer to choose colors to be used in the design.
Requirements
Must have
- Use the product shot and our branding...and a simple design!
Nice to have
- Want a "drinking an ice cold beer on a summer day" feel to this.

```html
<!DOCTYPE html>
<html lang="en">
<head>
<meta charset="utf-8">
<title>Frosk Brew Chill – The Fastest Way to Cool Beer Down</title>
<link href="https://fonts.googleapis.com/css2?family=Jost:ital,wght@0,700;0,800;0,900;1,800&display=swap" rel="stylesheet">
<style>
  :root {
    --sun-yellow: #ffd21f;
    --sun-orange: #f6901e;
    --deep-orange: #e8561c;
    --banner-black: #231f20;
    --ice-blue: #6dcff6;
    --ice-deep: #3aa6dd;
    --ice-pale: #d8f1fb;
    --alert-red: #ec1e4f;
    --paper-white: #ffffff;
    --ink-black: #1a1a1a;
    --logo-yellow: #e8ea1f;
  }
  html, body {
    margin: 0;
    padding: 0;
    width: 800px;
    height: 1200px;
    overflow: hidden;
    background: var(--sun-orange);
  }
  .poster {
    position: relative;
    width: 800px;
    height: 1200px;
    overflow: hidden;
    font-family: "Jost", "Futura", sans-serif;
  }
  .summer-backdrop {
    position: absolute;
    inset: 0;
    background:
      radial-gradient(circle at 300px 360px, #fff6c8 0, var(--sun-yellow) 90px, rgba(255,200,30,0) 320px),
      linear-gradient(115deg, var(--sun-yellow) 0%, var(--sun-orange) 45%, var(--deep-orange) 100%);
  }
  .headline-banner {
    position: absolute;
    left: 25px;
    top: 175px;
    width: 880px;
    height: 170px;
    margin: 0;
    padding-right: 110px;
    box-sizing: border-box;
    background: var(--banner-black);
    transform: rotate(-12deg);
    transform-origin: 0 50%;
    display: flex;
    flex-direction: column;
    justify-content: center;
    align-items: center;
    color: var(--ice-blue);
    font-weight: 800;
    line-height: 0.98;
    text-transform: uppercase;
    white-space: nowrap;
  }
  .headline-line-one { display: block; font-size: 72px; }
  .headline-line-two { display: block; font-size: 60px; }
  .ice-strip {
    position: absolute;
    left: 58px;
    top: 368px;
    width: 242px;
    height: 800px;
    background: var(--ice-blue);
  }
  .ice-photo {
    position: absolute;
    left: 76px;
    top: 575px;
    width: 208px;
    height: 580px;
    background: linear-gradient(160deg, var(--ice-pale) 0%, var(--ice-blue) 45%, var(--ice-deep) 100%);
  }
  .temperature {
    position: absolute;
    left: 76px;
    top: 384px;
    width: 210px;
    height: 80px;
    display: flex;
    align-items: center;
    justify-content: center;
    color: var(--alert-red);
    font-weight: 800;
    font-size: 68px;
    line-height: 1;
  }
  .time-claim {
    position: absolute;
    left: 80px;
    top: 478px;
    width: 208px;
    height: 96px;
    background: var(--paper-white);
    display: flex;
    flex-direction: column;
    justify-content: center;
    align-items: center;
    font-style: italic;
    font-weight: 800;
    font-size: 34px;
    line-height: 1.08;
    color: var(--ink-black);
    text-transform: uppercase;
  }
  .product-shot {
    position: absolute;
    left: 322px;
    top: 560px;
    width: 350px;
    height: 580px;
  }
  .call-to-action {
    position: absolute;
    left: 60px;
    top: 705px;
    margin: 0;
    color: var(--ink-black);
    font-weight: 900;
    text-transform: uppercase;
    line-height: 0.9;
    white-space: nowrap;
  }
  .call-to-action span { display: block; }
  .cta-small { font-size: 70px; letter-spacing: -1px; }
  .cta-medium { font-size: 92px; letter-spacing: -1px; margin-top: 14px; }
  .cta-large { font-size: 134px; letter-spacing: -2px; margin-top: 2px; }
  .brand-mark {
    position: absolute;
    left: 580px;
    top: 975px;
    width: 190px;
    height: 190px;
    border-radius: 50%;
    background: var(--banner-black);
    display: flex;
    align-items: center;
    justify-content: center;
    text-align: center;
    color: var(--logo-yellow);
    font-weight: 800;
    font-size: 27px;
    line-height: 1.05;
    text-transform: uppercase;
  }
</style>
</head>
<body>
  <main class="poster">
    <div class="summer-backdrop" role="img" aria-label="Sunny tropical sky with palm tree silhouettes in warm yellow and orange"></div>

    <h1 class="headline-banner">
      <span class="headline-line-one">The Fastest Way</span>
      <span class="headline-line-two">To Cool Beer Down!</span>
    </h1>

    <div class="ice-strip"></div>
    <div class="ice-photo" role="img" aria-label="Close-up of clear blue ice cubes"></div>
    <div class="temperature">55°F</div>
    <div class="time-claim"><span>In just</span><span>a minute</span></div>

    <svg class="product-shot" viewBox="0 0 350 580" role="img" aria-label="Glass of lime-flavoured beer with a splash as a flavoured ice cube drops in">
      <defs>
        <linearGradient id="beerTone" x1="0" x2="0" y1="0" y2="1">
          <stop offset="0" stop-color="#fffbe6"/>
          <stop offset="0.25" stop-color="#f6e08a"/>
          <stop offset="1" stop-color="#e8c447"/>
        </linearGradient>
      </defs>
      <path d="M5 15 h340 l-22 555 h-296 z" fill="url(#beerTone)"/>
    </svg>

    <p class="call-to-action">
      <span class="cta-small">Check the</span>
      <span class="cta-medium">Freezer</span>
      <span class="cta-large">Now!</span>
    </p>

    <div class="brand-mark">Frosk<br>Brew<br>Chill</div>
  </main>
</body>
</html>
```